Business Card Design for Photographer

Updating business card design. Must use included logo. We're a luxury wedding photography business. Elegancy, luxury, consistency are messages we wish to convey.

Visit our website at www.colbyvarnway.com to familiarize yourself more with our brand design currently (fonts, colors etc.). This is what we want to maintain.

Target Market(s)

Luxury Brides and Grooms

Industry/Entity Type

Wedding

Contact Information for Business Card

Current logo (attached to brief)
Name: Colby Varnway
Phone: 5208813047
website/blog
Email

Requirements
Must have
• Current logo (attached to brief)
• Name: Colby Varnway
• Phone: 5208813047
• website/blog
• Email
• Instagram username
Should not have
• bright colors, fonts that don't suit our brand (visit www.colbyvarnway.com)

```html
<!DOCTYPE html>
<html lang="en">
<head>
<meta charset="utf-8">
<title>Colby Varnway Photographers – Business Card</title>
<link rel="stylesheet" href="https://fonts.googleapis.com/css2?family=Marcellus&family=Open+Sans:wght@400&display=swap">
<style>
  :root {
    --bg: #d6d6d6;
    --card: #2a2a2a;
    --card-deep: #1f1f1f;
    --pill: #1a1a1a;
    --brand-text: #b9b9b9;
    --contact-text: #e6e6e6;
    --icon: #cfcfcf;
    --mark: #9a9a9a;
    --photo-a: #6f7f5a;
    --photo-b: #c9c4bd;
    --photo-c: #8a8f99;
    --dot-1: #6f7d99;
    --dot-2: #7f9bb0;
    --dot-3: #8c8a86;
    --dot-4: #a07a7a;
  }
  * { margin: 0; padding: 0; box-sizing: border-box; }
  html, body { width: 1200px; height: 747px; overflow: hidden; }
  body {
    background: var(--bg);
    display: flex;
    align-items: center;
    justify-content: center;
    gap: 60px;
  }
  .card {
    position: relative;
    width: 366px;
    height: 640px;
    background: radial-gradient(ellipse at 50% 20%, #333 0%, var(--card) 55%, var(--card-deep) 100%);
    overflow: hidden;
    box-shadow: 0 6px 18px rgba(0,0,0,.25);
  }
  .card svg.art { position: absolute; inset: 0; }
  .brand {
    position: absolute;
    left: 0; right: 0; top: 34px;
    text-align: center;
    color: var(--brand-text);
    font-family: "Marcellus", serif;
  }
  .brand-mark {
    display: block;
    width: 40px; height: 40px;
    margin: 0 auto 12px;
    background: var(--mark);
  }
  .brand-name { font-size: 22px; letter-spacing: 4px; text-transform: uppercase; }
  .brand-tag { font-size: 11px; letter-spacing: 6px; text-transform: uppercase; margin-top: 4px; }
  .contacts {
    position: absolute;
    left: 18px; right: 0; top: 420px;
    list-style: none;
  }
  .contact {
    display: flex;
    align-items: center;
    height: 34px;
    margin-bottom: 14px;
    background: var(--pill);
    border-radius: 17px 0 0 17px;
    color: var(--contact-text);
    font-family: "Open Sans", sans-serif;
    font-size: 15px;
  }
  .contact-icon {
    width: 34px; height: 34px;
    border-radius: 50%;
    background: #2f2f2f;
    display: flex; align-items: center; justify-content: center;
    margin-right: 12px;
  }
  .social {
    position: absolute;
    left: 0; right: 18px; top: 570px;
    height: 40px;
    background: var(--pill);
    border-radius: 0 20px 20px 0;
    display: flex; align-items: center; justify-content: flex-end;
    gap: 10px; padding-right: 14px;
  }
  .social-dot { width: 26px; height: 26px; border-radius: 50%; }
  .dot-1 { background: var(--dot-1); }
  .dot-2 { background: var(--dot-2); }
  .dot-3 { background: var(--dot-3); }
  .dot-4 { background: var(--dot-4); }
</style>
</head>
<body>

<section class="card card-front">
  <svg class="art" width="366" height="640" viewBox="0 0 366 640">
    <defs>
      <linearGradient id="photoCouple" x1="0" y1="0" x2="1" y2="1">
        <stop offset="0" stop-color="var(--photo-a)"/>
        <stop offset="0.6" stop-color="var(--photo-b)"/>
        <stop offset="1" stop-color="#9c9c98"/>
      </linearGradient>
    </defs>
    <path role="img" aria-label="Photo of a bride and groom embracing beside a white vintage car in a garden"
          fill="url(#photoCouple)"
          d="M0,215 Q183,160 366,205 L366,400 Q200,300 0,300 Z"/>
  </svg>
  <header class="brand">
    <span class="brand-mark"></span>
    <div class="brand-name">Colby Varnway</div>
    <div class="brand-tag">Photographers</div>
  </header>
  <ul class="contacts">
    <li class="contact">
      <span class="contact-icon">
        <svg width="18" height="18" viewBox="0 0 24 24"><path fill="var(--icon)" d="M6.6 10.8a15 15 0 0 0 6.6 6.6l2.2-2.2c.3-.3.7-.4 1-.2 1.1.4 2.3.6 3.6.6.6 0 1 .4 1 1V20c0 .6-.4 1-1 1A17 17 0 0 1 3 4c0-.6.4-1 1-1h3.5c.6 0 1 .4 1 1 0 1.3.2 2.5.6 3.6.1.3 0 .7-.2 1z"/></svg>
      </span>(520) 881-3047
    </li>
    <li class="contact">
      <span class="contact-icon">
        <svg width="18" height="14" viewBox="0 0 18 14"><rect x="1" y="1" width="16" height="12" fill="none" stroke="var(--icon)" stroke-width="1.6"/><path d="M1 1 L9 8 L17 1" fill="none" stroke="var(--icon)" stroke-width="1.6"/></svg>
      </span>colby@colbyvarnway.com
    </li>
    <li class="contact">
      <span class="contact-icon">
        <svg width="18" height="18" viewBox="0 0 20 20" fill="none" stroke="var(--icon)" stroke-width="1.4"><circle cx="10" cy="10" r="8"/><ellipse cx="10" cy="10" rx="3.5" ry="8"/><path d="M2 10h16M3.5 5.5h13M3.5 14.5h13"/></svg>
      </span>www.colbyvarnway.com
    </li>
  </ul>
</section>

<section class="card card-back">
  <svg class="art" width="366" height="640" viewBox="0 0 366 640">
    <defs>
      <linearGradient id="photoParty" x1="0" y1="0" x2="0" y2="1">
        <stop offset="0" stop-color="var(--photo-a)"/>
        <stop offset="0.55" stop-color="var(--photo-c)"/>
        <stop offset="1" stop-color="#6f8a4e"/>
      </linearGradient>
    </defs>
    <path role="img" aria-label="Photo of bridesmaids in grey gowns holding bouquets in a garden"
          fill="url(#photoParty)"
          d="M0,250 Q200,180 366,290 L366,490 Q180,440 0,520 Z"/>
  </svg>
  <header class="brand">
    <span class="brand-mark"></span>
    <div class="brand-name">Colby Varnway</div>
    <div class="brand-tag">Photographers</div>
  </header>
  <div class="social">
    <span class="social-dot dot-1"></span>
    <span class="social-dot dot-2"></span>
    <span class="social-dot dot-3"></span>
    <span class="social-dot dot-4"></span>
  </div>
</section>

</body>
</html>
```